Brand Design/Redesign

Design and/or redesign an identity for product and organisation
Create visual identity (colours, fonts), website, mobile app, web application, online campaigns, social media.

I have given a sample wireframe for you to use so that we can really get a sense of the colour palette you are choosing and how it will look in a live context.

Considerations when Choosing:
Brand is for Gen Z -
With a particular focus on 16 - 18 years old.

There will be a commercial portal for Business to use also.

Please outline in a short paragraph why you choose the colours and their relationship to our target audience.

Selected winner to produce Brand Identity Document

Please see document attached.

Target Market(s)

Gen Z 16 - 18 yearolds

Industry/Entity Type

Social Media

Requirements
Must have
• Colour Palette & Font Selections, Visual of Colour Palette & Winner to produce Brand Identity Doc
Nice to have
• Really Cool, Edgy and Appeal to aYoung Audience
Should not have
• A corporate feel to it

```html
<!DOCTYPE html>
<html lang="en">
<head>
<meta charset="utf-8">
<title>VOLTA – App Screens</title>
<link href="https://fonts.googleapis.com/css2?family=Oswald:wght@500;600;700&family=Montserrat:wght@400;500;600;700&display=swap" rel="stylesheet">
<style>
  :root{
    --pink:#f5468e;
    --purple:#b43ee8;
    --grad:linear-gradient(110deg,#f5468e 0%,#d844c4 55%,#b43ee8 100%);
    --grad-btn:linear-gradient(90deg,#b43ee8 0%,#f5468e 100%);
    --stage:#e9e8ee;
  }
  .theme-dark{
    --bg:#2b2a3a; --card:#232232; --field:#242333; --text:#ffffff;
    --muted:#9a98aa; --line:#4a4860; --tab:#262535; --icon:#8a889c;
    --card-shadow:none;
  }
  .theme-light{
    --bg:#ffffff; --card:#ffffff; --field:#ffffff; --text:#1b1a24;
    --muted:#77768a; --line:#d9d8e0; --tab:#ffffff; --icon:#2b2a3a;
    --card-shadow:0 2px 8px rgba(40,30,60,.12);
  }
  *{box-sizing:border-box;margin:0;padding:0}
  html,body{width:1068px;height:1200px;overflow:hidden;background:var(--stage);
    font-family:"Montserrat",sans-serif}
  .canvas{width:1068px;height:1200px;display:flex;flex-direction:column;justify-content:center;gap:40px;padding:0 50px}
  .row{display:flex;gap:34px;justify-content:center}
  .screen{width:300px;height:540px;background:var(--bg);color:var(--text);position:relative;
    overflow:hidden;border-radius:14px;box-shadow:0 10px 30px rgba(40,20,70,.18)}
  .icon{width:14px;height:14px;fill:none;stroke:currentColor;stroke-width:1.8;stroke-linecap:round;stroke-linejoin:round}
  .wordmark{font-family:"Oswald",sans-serif;font-weight:700;color:var(--pink);letter-spacing:.5px;line-height:1}

  /* Login */
  .login{padding:34px 20px 0;text-align:center}
  .login .wordmark{font-size:52px;margin-bottom:28px}
  .login h1{font-family:"Oswald",sans-serif;font-weight:700;font-size:19px;letter-spacing:.3px}
  .login .sub{font-size:12px;color:var(--muted);margin:6px 0 22px;line-height:1.35}
  .theme-light .login .sub{color:var(--text)}
  .field{height:40px;background:var(--field);border-radius:6px;display:flex;align-items:center;gap:8px;
    padding:0 12px;font-size:9.5px;color:var(--muted);margin-bottom:12px;box-shadow:var(--card-shadow);text-align:left}
  .field .icon{color:var(--pink);width:12px;height:12px}
  .forgot{font-size:9.5px;color:var(--muted);text-align:right;margin:-6px 0 24px}
  .btn-main{height:42px;border-radius:21px;background:var(--grad-btn);color:#fff;font-weight:600;font-size:13px;
    display:flex;align-items:center;justify-content:center}
  .divider{display:flex;align-items:center;gap:8px;font-size:9.5px;color:var(--muted);margin:26px 10px 18px}
  .divider::before,.divider::after{content:"";flex:1;height:1px;background:var(--muted);opacity:.6}
  .socials{display:flex;justify-content:center;gap:18px;margin-bottom:24px}
  .socials span{width:32px;height:32px;border-radius:50%;background:#111018}
  .theme-dark .socials span{background:#1a1926}
  .socials span.active{background:var(--pink)}
  .register{font-size:9.5px;color:var(--text)}
  .register b{color:var(--pink);font-weight:600;text-decoration:underline}

  /* Shared app chrome */
  .status{display:flex;justify-content:space-between;padding:14px 18px 0;font-size:10px;font-weight:600}
  .topbar{display:flex;align-items:center;gap:10px;padding:10px 12px 0}
  .topbar .icon{color:var(--muted)}
  .topbar .wordmark{margin-left:auto;font-size:26px}
  .toggle{display:flex;border:1px solid var(--pink);border-radius:12px;overflow:hidden;font-size:9.5px;font-weight:600}
  .toggle span{padding:5px 12px}
  .toggle .on{background:var(--pink);color:#fff}
  .search{margin:12px 12px 0;height:34px;border:1px solid var(--line);border-radius:17px;display:flex;align-items:center;
    gap:8px;padding:0 14px;font-size:11px;color:var(--muted)}
  .theme-light .search{box-shadow:var(--card-shadow);color:var(--text)}
  .tabbar{position:absolute;left:0;right:0;bottom:0;height:50px;background:var(--tab);display:flex;justify-content:space-around;
    align-items:center;color:var(--icon)}
  .theme-light .tabbar{box-shadow:0 -2px 8px rgba(40,30,60,.08)}
  .tabbar .icon{width:18px;height:18px}
  .tabbar .current{color:var(--pink);border-bottom:2px solid var(--pink);padding-bottom:3px}

  /* Home */
  .challenge{margin:12px 12px 0;height:134px;border-radius:8px;background:var(--grad);position:relative;overflow:hidden;padding:12px;color:#fff}
  .challenge::after{content:"";position:absolute;right:-30px;bottom:-40px;width:110px;height:110px;border-radius:50%;background:#d63cc8;opacity:.7}
  .challenge h2{font-family:"Oswald",sans-serif;font-weight:600;font-size:18px}
  .challenge p{font-size:9.5px;font-weight:600;line-height:1.3;margin:12px 0 10px;width:150px}
  .challenge .cta{display:inline-flex;align-items:center;gap:10px;background:#fff;color:#1b1a24;font-size:9px;font-weight:600;
    padding:5px 8px 5px 14px;border-radius:12px;position:relative;z-index:1}
  .challenge .cta i{width:11px;height:11px;border-radius:50%;background:var(--purple);display:block}
  .challenge .art{position:absolute;right:10px;top:10px;width:42px;height:42px;border-radius:6px;
    background:linear-gradient(135deg,#ffffff,#ffe3ef);z-index:1}
  .tiles{display:grid;grid-template-columns:1fr 1fr;gap:8px;margin:10px 12px 0}
  .tile{background:var(--card);border-radius:6px;height:58px;padding:8px;position:relative;box-shadow:var(--card-shadow);font-size:9.5px}
  .tile.tall{height:86px}
  .avatar{width:24px;height:24px;border-radius:50%;background:linear-gradient(135deg,#8d7a70,#cdbfb6)}
  .bell{position:absolute;right:10px;top:10px;width:22px;height:22px;border-radius:5px;background:var(--grad-btn);color:#fff;
    display:flex;align-items:center;justify-content:center}
  .bell .icon{width:11px;height:11px}
  .bell b{position:absolute;top:-4px;right:-4px;background:#fff;color:var(--pink);font-size:7px;width:11px;height:11px;border-radius:50%;
    display:flex;align-items:center;justify-content:center}
  .greet{position:absolute;left:8px;bottom:8px;color:var(--muted)}
  .theme-light .greet{color:var(--text)}
  .earn{background:#2d2c3e;color:#fff}
  .earn .amount{font-size:15px;font-weight:600;display:flex;align-items:center;gap:5px}
  .earn .amount i{width:10px;height:10px;border:2px solid #fff;border-radius:50%;display:block}
  .earn .last{position:absolute;right:8px;top:8px;font-size:6px;text-align:right;line-height:1.3}
  .earn .note{position:absolute;left:8px;bottom:6px;font-size:9px;line-height:1.1;color:#d9d8e0}
  .brand-dot{width:24px;height:24px;border-radius:50%;background:#111018;border:2px solid var(--pink)}
  .follow{position:absolute;right:8px;top:10px;background:var(--pink);color:#fff;font-size:7px;font-weight:600;padding:3px 8px;border-radius:8px}
  .count{position:absolute;right:16px;top:30px;text-align:center;font-size:12px;font-weight:600;line-height:1}
  .count small{display:block;font-size:5px;font-weight:500;color:var(--muted)}
  .meta{position:absolute;left:8px;bottom:7px;font-size:7.5px;line-height:1.3;color:var(--muted);font-weight:500}
  .meta b{color:var(--text);font-weight:600}
  .tag{position:absolute;right:8px;top:14px;font-size:7.5px;font-weight:500;color:var(--muted)}

  /* Help */
  .help-head{display:flex;align-items:flex-start;gap:10px;padding:16px 12px 0}
  .help-head .icon{color:var(--muted);margin-top:5px}
  .help-head h2{font-family:"Oswald",sans-serif;font-weight:500;font-size:18px;line-height:1.25;letter-spacing:.3px}
  .theme-dark .help-head h2{color:#bdbbca}
  .help-head .wordmark{margin-left:auto;font-size:26px}
  .cats{display:flex;gap:10px;margin:16px 0 0 12px}
  .cat{flex:0 0 78px;height:82px;background:var(--card);border-radius:6px;padding:8px;display:flex;flex-direction:column;
    justify-content:space-between;font-size:9.5px;font-weight:600;color:var(--muted);box-shadow:var(--card-shadow)}
  .cat .icon{width:18px;height:18px;color:var(--text)}
  .theme-light .cat .icon{color:var(--pink)}
  .cat.on{background:var(--grad);color:#fff}
  .cat.on .icon{color:#fff}
  .section{font-family:"Oswald",sans-serif;font-weight:500;font-size:15px;margin:18px 12px 6px}
  .theme-dark .section{color:#bdbbca}
  .item{display:flex;align-items:center;gap:10px;padding:6px 14px 6px 12px;font-size:11px;color:var(--muted)}
  .theme-light .item{color:var(--text)}
  .item i{width:22px;height:22px;border-radius:50%;background:#111018;color:#fff;display:flex;align-items:center;justify-content:center}
  .theme-light .item i{background:var(--pink)}
  .item i .icon{width:11px;height:11px}
  .item .chev{margin-left:auto;color:var(--muted);width:10px;height:10px}
</style>
</head>
<body>
<svg width="0" height="0" style="position:absolute" aria-hidden="true">
  <symbol id="i-user" viewBox="0 0 24 24"><circle cx="12" cy="8" r="4"/><path d="M4 21c0-4 4-6 8-6s8 2 8 6"/></symbol>
  <symbol id="i-eye" viewBox="0 0 24 24"><path d="M2 12s4-7 10-7 10 7 10 7-4 7-10 7S2 12 2 12z"/><circle cx="12" cy="12" r="3"/><path d="M4 20L20 4"/></symbol>
  <symbol id="i-back" viewBox="0 0 24 24"><path d="M20 12H4M10 6l-6 6 6 6"/></symbol>
  <symbol id="i-search" viewBox="0 0 24 24"><circle cx="11" cy="11" r="7"/><path d="M20 20l-4-4"/></symbol>
  <symbol id="i-home" viewBox="0 0 24 24"><path d="M3 11l9-8 9 8M5 10v10h5v-6h4v6h5V10"/></symbol>
  <symbol id="i-cart" viewBox="0 0 24 24"><path d="M2 4h3l3 11h11l2-8H6"/><circle cx="9" cy="20" r="1.5"/><circle cx="18" cy="20" r="1.5"/></symbol>
  <symbol id="i-compass" viewBox="0 0 24 24"><circle cx="12" cy="12" r="9"/><path d="M15.5 8.5l-2 5-5 2 2-5z"/></symbol>
  <symbol id="i-bell" viewBox="0 0 24 24"><path d="M6 17V11a6 6 0 0112 0v6l2 2H4zM10 21h4"/></symbol>
  <symbol id="i-doc" viewBox="0 0 24 24"><rect x="4" y="3" width="12" height="16" rx="2"/><path d="M7 8h6M7 12h6M14 14h6v7h-6z"/></symbol>
  <symbol id="i-globe" viewBox="0 0 24 24"><circle cx="12" cy="12" r="9"/><path d="M3 12h18M12 3c3 3 3 15 0 18M12 3c-3 3-3 15 0 18"/></symbol>
  <symbol id="i-phone" viewBox="0 0 24 24"><rect x="7" y="2" width="10" height="20" rx="2"/><path d="M11 18h2"/></symbol>
  <symbol id="i-screen" viewBox="0 0 24 24"><rect x="3" y="4" width="18" height="13" rx="2"/><path d="M8 21h8M7 9h4M7 12h6"/></symbol>
  <symbol id="i-mail" viewBox="0 0 24 24"><rect x="3" y="5" width="18" height="14" rx="2"/><path d="M3 7l9 6 9-6"/></symbol>
  <symbol id="i-wallet" viewBox="0 0 24 24"><rect x="3" y="7" width="18" height="13" rx="2"/><path d="M6 7l9-4 2 4M16 13h3"/></symbol>
  <symbol id="i-chev" viewBox="0 0 24 24"><path d="M9 5l7 7-7 7"/></symbol>
</svg>

<main class="canvas">
  <!-- two themes, identical structure -->
  <section class="row theme-dark">
    <article class="screen login">
      <div class="wordmark">VOLTA</div>
      <h1>HELLO AGAIN</h1>
      <p class="sub">Welcome back you've<br>been missed!</p>
      <div class="field"><svg class="icon"><use href="#i-user"/></svg>Enter Username</div>
      <div class="field"><svg class="icon"><use href="#i-eye"/></svg>Password</div>
      <p class="forgot">Forget Password?</p>
      <div class="btn-main">Sign In</div>
      <p class="divider">Or Continue With</p>
      <div class="socials"><span></span><span class="active"></span><span></span></div>
      <p class="register">Not a member? <b>Register Now</b></p>
    </article>

    <article class="screen home">
      <div class="status"><span>9:41</span><span>●●</span></div>
      <div class="topbar">
        <svg class="icon"><use href="#i-back"/></svg>
        <div class="toggle"><span class="on">For You</span><span>News</span></div>
        <span class="wordmark">VOLTA</span>
      </div>
      <div class="search"><svg class="icon"><use href="#i-search"/></svg>Search</div>
      <div class="challenge">
        <h2>Daily Challenge</h2>
        <p>Participate in challenges to learn more about your friends!</p>
        <span class="cta">Start Now <i></i></span>
        <div class="art" role="img" aria-label="Rocket illustration"></div>
      </div>
      <div class="tiles">
        <div class="tile">
          <div class="avatar" role="img" aria-label="Profile photo"></div>
          <span class="bell"><svg class="icon"><use href="#i-bell"/></svg><b>8</b></span>
          <span class="greet">Hey, Jamie!</span>
        </div>
        <div class="tile earn">
          <div class="amount"><i></i>543</div>
          <div class="last">Last earning<br>120</div>
          <div class="note">Lumi advertisement<br>review</div>
        </div>
        <div class="tile tall">
          <div class="brand-dot"></div>
          <span class="follow">Follow</span>
          <div class="count">23<small>Action<br>Providing</small></div>
          <div class="meta"><b>Stride Co.</b><br>#Sport #lifestyle</div>
        </div>
        <div class="tile tall">
          <div class="brand-dot"></div>
          <span class="tag">VOLTA</span>
          <div class="meta"><b>My First action<br>title</b><br>5 days remaining</div>
        </div>
      </div>
      <nav class="tabbar">
        <svg class="icon current"><use href="#i-home"/></svg>
        <svg class="icon"><use href="#i-cart"/></svg>
        <svg class="icon"><use href="#i-compass"/></svg>
        <svg class="icon"><use href="#i-user"/></svg>
      </nav>
    </article>

    <article class="screen help">
      <div class="help-head">
        <svg class="icon"><use href="#i-back"/></svg>
        <h2>What can we help<br>you with?</h2>
        <span class="wordmark">VOLTA</span>
      </div>
      <div class="search"><svg class="icon"><use href="#i-search"/></svg>Search</div>
      <div class="cats">
        <div class="cat on"><svg class="icon"><use href="#i-doc"/></svg>Search and<br>Play</div>
        <div class="cat"><svg class="icon"><use href="#i-globe"/></svg>Full Time<br>Games</div>
        <div class="cat"><svg class="icon"><use href="#i-phone"/></svg>Full Time<br>Fun</div>
      </div>
      <h3 class="section">Walkthroughs</h3>
      <div class="item"><i><svg class="icon"><use href="#i-phone"/></svg></i>Getting started with the app<svg class="icon chev"><use href="#i-chev"/></svg></div>
      <div class="item"><i><svg class="icon"><use href="#i-screen"/></svg></i>Run troubleshooting<svg class="icon chev"><use href="#i-chev"/></svg></div>
      <h3 class="section">Get In Touch</h3>
      <div class="item"><i><svg class="icon"><use href="#i-mail"/></svg></i>Send us an email<svg class="icon chev"><use href="#i-chev"/></svg></div>
      <div class="item"><i><svg class="icon"><use href="#i-wallet"/></svg></i>Make a payment details<svg class="icon chev"><use href="#i-chev"/></svg></div>
      <nav class="tabbar">
        <svg class="icon current"><use href="#i-home"/></svg>
        <svg class="icon"><use href="#i-cart"/></svg>
        <svg class="icon"><use href="#i-compass"/></svg>
        <svg class="icon"><use href="#i-user"/></svg>
      </nav>
    </article>
  </section>

  <section class="row theme-light">
    <article class="screen login">
      <div class="wordmark">VOLTA</div>
      <h1>HELLO AGAIN</h1>
      <p class="sub">Welcome back you've<br>been missed!</p>
      <div class="field"><svg class="icon"><use href="#i-user"/></svg>Enter Username</div>
      <div class="field"><svg class="icon"><use href="#i-eye"/></svg>Password</div>
      <p class="forgot">Forget Password?</p>
      <div class="btn-main">Sign In</div>
      <p class="divider">Or Continue With</p>
      <div class="socials"><span></span><span class="active"></span><span></span></div>
      <p class="register">Not a member? <b>Register Now</b></p>
    </article>

    <article class="screen home">
      <div class="status"><span>9:41</span><span>●●</span></div>
      <div class="topbar">
        <svg class="icon"><use href="#i-back"/></svg>
        <div class="toggle"><span class="on">For You</span><span>News</span></div>
        <span class="wordmark">VOLTA</span>
      </div>
      <div class="search"><svg class="icon"><use href="#i-search"/></svg>Search</div>
      <div class="challenge">
        <h2>Daily Challenge</h2>
        <p>Participate in challenges to learn more about your friends!</p>
        <span class="cta">Start Now <i></i></span>
        <div class="art" role="img" aria-label="Rocket illustration"></div>
      </div>
      <div class="tiles">
        <div class="tile">
          <div class="avatar" role="img" aria-label="Profile photo"></div>
          <span class="bell"><svg class="icon"><use href="#i-bell"/></svg><b>8</b></span>
          <span class="greet">Hey, Jamie!</span>
        </div>
        <div class="tile earn">
          <div class="amount"><i></i>543</div>
          <div class="last">Last earning<br>120</div>
          <div class="note">Lumi advertisement<br>review</div>
        </div>
        <div class="tile tall">
          <div class="brand-dot"></div>
          <span class="follow">Follow</span>
          <div class="count">23<small>Action<br>Providing</small></div>
          <div class="meta">Stride Co.<br><b>#Sport #lifestyle</b></div>
        </div>
        <div class="tile tall">
          <div class="brand-dot"></div>
          <span class="tag">VOLTA</span>
          <div class="meta">My First action<br>title<br><b>5 days remaining</b></div>
        </div>
      </div>
      <nav class="tabbar">
        <svg class="icon current"><use href="#i-home"/></svg>
        <svg class="icon"><use href="#i-cart"/></svg>
        <svg class="icon"><use href="#i-compass"/></svg>
        <svg class="icon"><use href="#i-user"/></svg>
      </nav>
    </article>

    <article class="screen help">
      <div class="help-head">
        <svg class="icon"><use href="#i-back"/></svg>
        <h2>What can we help<br>you with?</h2>
        <span class="wordmark">VOLTA</span>
      </div>
      <div class="search"><svg class="icon"><use href="#i-search"/></svg>Search</div>
      <div class="cats">
        <div class="cat on"><svg class="icon"><use href="#i-doc"/></svg>Search and<br>Play</div>
        <div class="cat"><svg class="icon"><use href="#i-globe"/></svg>Full Time<br>Games</div>
        <div class="cat"><svg class="icon"><use href="#i-phone"/></svg>Full Time<br>Fun</div>
      </div>
      <h3 class="section">Walkthroughs</h3>
      <div class="item"><i><svg class="icon"><use href="#i-phone"/></svg></i>Getting started with the app<svg class="icon chev"><use href="#i-chev"/></svg></div>
      <div class="item"><i><svg class="icon"><use href="#i-screen"/></svg></i>Run troubleshooting<svg class="icon chev"><use href="#i-chev"/></svg></div>
      <h3 class="section">Get In Touch</h3>
      <div class="item"><i><svg class="icon"><use href="#i-mail"/></svg></i>Send us an email<svg class="icon chev"><use href="#i-chev"/></svg></div>
      <div class="item"><i><svg class="icon"><use href="#i-wallet"/></svg></i>Make a payment details<svg class="icon chev"><use href="#i-chev"/></svg></div>
      <nav class="tabbar">
        <svg class="icon current"><use href="#i-home"/></svg>
        <svg class="icon"><use href="#i-cart"/></svg>
        <svg class="icon"><use href="#i-compass"/></svg>
        <svg class="icon"><use href="#i-user"/></svg>
      </nav>
    </article>
  </section>
</main>
</body>
</html>
```